Commercial Real Estate

We need a business card design for a new commercial real estate business that specializes in apartment building brokerage. Not individual units but the entire complex. We find and represent the owners existing buildings and well as new buyers for those buildings. The design should convey trust, integrity, knowledge and growth. It should be easily read.

Target Market(s)

40 to 65 years old

Industry/Entity Type

Real Estate

```html
<!DOCTYPE html>
<html lang="en">
<head>
<meta charset="utf-8">
<title>Harbrook Property Investments – Business Cards</title>
<link rel="stylesheet" href="https://fonts.googleapis.com/css2?family=Questrial&family=Source+Sans+3:wght@400;600&display=swap">
<style>
  :root {
    --canvas: #ffffff;
    --ink: #111111;
    --teal: #5cc6c6;
    --slate: #4e5c5c;
    --band-dark: #000000;
    --band-grey: #444444;
    --rule: #555555;
    --paper-light: #f4f4f4;
    --paper-mid: #d9d9d9;
    --tone-teal: #5f8e8c;
    --white: #ffffff;
  }
  * { box-sizing: border-box; margin: 0; padding: 0; }
  html, body { width: 1200px; height: 900px; overflow: hidden; background: var(--canvas); }
  body { position: relative; font-family: "Source Sans 3", "Helvetica Neue", Arial, sans-serif; color: var(--ink); }

  .card { position: absolute; overflow: hidden; }
  .card-portrait { left: 0; top: 0; width: 448px; height: 720px; }
  .card-landscape { left: 483px; top: 0; width: 717px; height: 447px; }

  .texture { position: absolute; inset: 0; }
  .card-portrait .texture {
    background: linear-gradient(180deg, var(--paper-light) 0%, #ececec 35%, var(--paper-mid) 62%, #a9bcbb 78%, var(--tone-teal) 88%, #b5cfcf 100%);
  }
  .card-landscape .texture {
    background: linear-gradient(90deg, var(--paper-light) 0%, #ececec 30%, var(--paper-mid) 55%, #9db5b4 72%, var(--tone-teal) 88%, #6f9997 100%);
  }

  .holder-name {
    position: absolute;
    font-family: "Questrial", "Century Gothic", sans-serif;
    font-variant: small-caps;
    letter-spacing: 0.18em;
    white-space: nowrap;
    line-height: 1;
  }
  .holder-name .first { color: var(--ink); }
  .holder-name .last { color: var(--teal); }
  .rule { position: absolute; height: 1px; background: var(--rule); }
  .role { position: absolute; font-size: 16px; color: var(--ink); white-space: nowrap; }

  .brand {
    position: absolute;
    display: flex;
    align-items: center;
    gap: 10px;
    font-weight: 600;
    color: var(--slate);
    letter-spacing: 0.06em;
    white-space: nowrap;
  }
  .brand-square { background: var(--teal); flex: none; }

  .contact-band { position: absolute; left: 0; right: 0; color: var(--white); white-space: nowrap; }
  .contact-band .label { color: var(--teal); }

  /* portrait */
  .card-portrait .holder-name { left: 0; right: 0; top: 66px; text-align: center; font-size: 44px; }
  .card-portrait .rule { left: 127px; width: 203px; top: 127px; }
  .card-portrait .role { left: 0; right: 0; top: 138px; text-align: center; }
  .card-portrait .brand { left: 0; right: 0; top: 440px; justify-content: center; font-size: 40px; }
  .card-portrait .brand-square { width: 26px; height: 26px; }
  .card-portrait .contact-band {
    top: 630px; height: 88px; background: var(--band-dark);
    display: grid; grid-template-columns: 201px 1fr; row-gap: 4px;
    padding: 12px 0 0 32px; font-size: 19px; line-height: 28px;
  }

  /* landscape */
  .url-tab {
    position: absolute; left: 255px; top: 0; width: 202px; height: 24px;
    background: var(--teal); color: var(--white); border-radius: 0 0 6px 6px;
    font-size: 15px; text-align: center; line-height: 22px;
  }
  .card-landscape .brand { left: 28px; top: 100px; font-size: 22px; gap: 8px; }
  .card-landscape .brand-square { width: 14px; height: 14px; }
  .card-landscape .role { left: 27px; top: 150px; }
  .card-landscape .holder-name { left: 210px; top: 225px; font-size: 44px; }
  .card-landscape .rule { left: 254px; width: 203px; top: 282px; }
  .card-landscape .contact-band {
    top: 384px; height: 63px; background: var(--band-grey);
    display: flex; align-items: center; gap: 8px; padding-left: 22px; font-size: 25px;
  }
  .card-landscape .contact-band .value { margin-right: 10px; }
</style>
</head>
<body>
  <section class="card card-portrait">
    <div class="texture" role="img" aria-label="Soft pattern of grey squares and circles fading into teal toward the bottom"></div>
    <h1 class="holder-name"><span class="first">John</span><span class="last">Doe</span></h1>
    <div class="rule"></div>
    <p class="role">Property Manager</p>
    <div class="brand"><span class="brand-square"></span>HARBROOK</div>
    <div class="contact-band">
      <span><span class="label">email</span>&nbsp; jd@harbrook.com</span>
      <span><span class="label">web</span>&nbsp; www.harbrook.com</span>
      <span><span class="label">direct</span>&nbsp; 123456789</span>
      <span><span class="label">office</span>&nbsp; 123456789</span>
    </div>
  </section>

  <section class="card card-landscape">
    <div class="texture" role="img" aria-label="Soft pattern of grey squares and circles deepening into teal toward the right"></div>
    <div class="url-tab">www.harbrook.com</div>
    <div class="brand"><span class="brand-square"></span>HARBROOK</div>
    <p class="role">Property Manager</p>
    <h1 class="holder-name"><span class="first">John</span><span class="last">Doe</span></h1>
    <div class="rule"></div>
    <div class="contact-band">
      <span class="label">office</span><span class="value">123456789</span>
      <span class="label">direct</span><span class="value">123456789</span>
      <span class="label">email</span><span class="value">jd@harbrook.com</span>
    </div>
  </section>
</body>
</html>
```